Rory's Personal Training -> also needs a logo

Services Frankston, Mornington, and Somerville

Specializes in in-home personal training

BlastCore style workouts

Not really preferential colors but needs to look modern and not stock photo

Training

• 30% off first time customers on a package of 10

```html
<!DOCTYPE html>
<html lang="en">
<head>
<meta charset="utf-8">
<title>Rory's Personal Training</title>
<link rel="stylesheet" href="https://fonts.googleapis.com/css2?family=Archivo+Black&family=Jost:wght@300;400;600&family=Arimo:wght@700&display=swap">
<style>
  :root {
    --ink-dark: #161b1a;
    --panel: #1d2321;
    --steel-deep: #2a3331;
    --steel-mid: #55635f;
    --steel-light: #b9c6c2;
    --jade: #2c7a5f;
    --text-light: #e6ecea;
    --text-soft: #d7dfdc;
    --logo-grey: #5b6261;
  }
  html, body {
    margin: 0;
    padding: 0;
    width: 1200px;
    height: 900px;
    overflow: hidden;
    background: var(--ink-dark);
  }
  .flyer {
    position: relative;
    width: 1200px;
    height: 900px;
    overflow: hidden;
  }
  .backdrop {
    position: absolute;
    inset: 0;
    width: 1200px;
    height: 900px;
  }
  .brand {
    position: absolute;
    top: 130px;
    left: 0;
    width: 1200px;
    text-align: center;
    font-family: "Archivo Black", sans-serif;
    color: var(--logo-grey);
    margin: 0;
    line-height: 1;
  }
  .brand-name {
    display: block;
    font-size: 200px;
    letter-spacing: 2px;
  }
  .brand-tagline {
    display: block;
    margin-top: 4px;
    font-size: 50px;
    letter-spacing: 4px;
  }
  .details {
    position: absolute;
    left: 60px;
    top: 598px;
    font-family: "Jost", sans-serif;
    color: var(--text-soft);
  }
  .details h2 {
    margin: 0;
    font-size: 32px;
    font-weight: 600;
    line-height: 1.1;
    text-transform: uppercase;
  }
  .details p {
    margin: 0 0 14px;
    font-size: 31px;
    font-weight: 300;
    line-height: 1.2;
    text-transform: uppercase;
    letter-spacing: 0.5px;
  }
  .offer {
    position: absolute;
    right: 36px;
    top: 622px;
    width: 305px;
    text-align: right;
    color: var(--text-light);
  }
  .offer-amount {
    margin: 0;
    font-family: "Jost", sans-serif;
    font-weight: 300;
    font-size: 84px;
    line-height: 0.86;
  }
  .offer-rule {
    border: 0;
    border-top: 3px solid var(--text-light);
    margin: 10px 0 8px;
  }
  .offer-terms {
    margin: 0;
    font-family: "Arimo", sans-serif;
    font-weight: 700;
    font-size: 24px;
    line-height: 1.45;
  }
</style>
</head>
<body>
<main class="flyer">
  <svg class="backdrop" viewBox="0 0 1200 900" aria-hidden="false">
    <defs>
      <radialGradient id="steel-glow" cx="0.6" cy="0.55" r="0.75">
        <stop offset="0" stop-color="#9fb0ab"/>
        <stop offset="0.45" stop-color="#5f716b"/>
        <stop offset="1" stop-color="#1f2725"/>
      </radialGradient>
      <linearGradient id="band-glow" x1="0" y1="1" x2="1" y2="0">
        <stop offset="0" stop-color="#3f6a5c"/>
        <stop offset="0.5" stop-color="#a9bcb6"/>
        <stop offset="1" stop-color="#6d8a80"/>
      </linearGradient>
    </defs>
    <rect class="texture-field" width="1200" height="900" fill="url(#steel-glow)" role="img" aria-label="Metallic diamond lattice texture in grey and jade green"/>
    <polygon class="texture-band" points="800,575 1200,505 1200,505 830,900 490,900" fill="url(#band-glow)" role="img" aria-label="Bright diagonal strip of the diamond lattice texture"/>
    <polygon class="info-panel" points="0,575 800,575 490,900 0,900" fill="var(--panel)"/>
    <polygon class="offer-panel" points="1200,505 1200,900 830,900" fill="var(--panel)"/>
  </svg>

  <h1 class="brand">
    <span class="brand-name">RORYS</span>
    <span class="brand-tagline">PERSONAL TRAINING</span>
  </h1>

  <section class="details">
    <h2>Services:</h2>
    <p>Frankston - Mornington,<br>and Somerville</p>
    <h2>Specializes in:</h2>
    <p>In-home personal training<br>BlastCore style workouts</p>
  </section>

  <aside class="offer">
    <p class="offer-amount">30%<br>OFF</p>
    <hr class="offer-rule">
    <p class="offer-terms">first time customers<br>on a package of 10</p>
  </aside>
</main>
</body>
</html>
```